Personal Injury Law Firm Marketing Postcards

Looking for 4 different high quality graphic postcards (print on both sides of 4"x6" postcard to market a Personal Injury Lawyer (Walter Gimsby). These will be placed on cars and in stores on stands. My photo and/or stock images.... We are targeting People who have been injured in automobile accidents, motorcycle accidents, slip and fall (wet/greasy floors indoors in supermarkets, restaurants, etc., snow and ice outdoors on sidewalks) trip and fall cases on dangerous staircases. indoor/outdoor, dog bite injuries. ( I like the use of stock images of these type of injury causing accidents. You can use following language "Serving People Injured in NY & NJ" . Millions of Dollars Recovered, Free Consultation and No Fee Unless We Recover Money! Phone number to be displayed (555) 418-3062 "call or text" Available 24 hours a day 7 days per week. May also want to mention that we can take over your case from another lawyer if you are not satisfied with your current attorney. There should be a small space in corner which has a space for my marketing person to handwrite in their reference code.

Target Market(s)

18-75 years old - densely populated major city

Industry/Entity Type

Legal

Font styles to use
Other font styles liked:
• Please use logo style that I uploaded.. Please do not just cut parts of my website out and use them. Do not use LOGO from my website

Colors
0054AA
0677BA
7BADD7
CADEEF
E8F1F8
00AB8E
00BBA5
67D7C9
C6EFE9
E9F9F6

Requirements
Must have
• Professional Appearance

```html
<!DOCTYPE html>
<html lang="en">
<head>
<meta charset="utf-8">
<title>Walter Gimsby – Dog Bite Injury Postcard</title>
<link rel="stylesheet" href="https://fonts.googleapis.com/css2?family=Roboto+Condensed:wght@700&family=Inter:wght@400;500&display=swap">
<style>
  :root {
    --navy: #1f3062;
    --gold: #d1ac6b;
    --gold-deep: #c29d55;
    --white: #ffffff;
    --photo-fur: #b98a4e;
    --photo-grey: #8d8b86;
  }
  * { margin: 0; padding: 0; box-sizing: border-box; }
  html, body { width: 1200px; height: 816px; overflow: hidden; background: var(--white); }
  .postcard { position: relative; width: 1200px; height: 816px; background: var(--white); overflow: hidden; }

  .frame {
    position: absolute; left: 0; top: 52px; width: 597px; height: 764px;
    background: var(--navy);
    border-top-right-radius: 195px 205px;
  }
  .photo {
    position: absolute; left: 0; top: 77px; width: 573px; height: 414px;
    border-top-right-radius: 170px 180px;
    background: linear-gradient(120deg, var(--photo-grey) 0%, #a59a8a 30%, var(--photo-fur) 60%, #7c5a34 100%);
  }
  .info-panel {
    position: absolute; left: 0; top: 491px; width: 573px; height: 325px;
    background: var(--gold);
  }
  .hours-icon { position: absolute; left: 86px; top: 496px; width: 94px; height: 94px; }
  .headline {
    position: absolute; left: 194px; top: 508px; width: 370px;
    font-family: "Roboto Condensed", sans-serif; font-weight: 700;
    font-size: 36px; line-height: 38px; color: var(--navy); letter-spacing: -0.6px;
    white-space: nowrap;
  }
  .takeover {
    position: absolute; left: 90px; top: 596px; width: 470px;
    font-family: "Inter", sans-serif; font-weight: 400;
    font-size: 19px; line-height: 24px; color: var(--navy);
  }
  .contact-icon { position: absolute; left: 86px; top: 675px; width: 80px; height: 80px; }
  .phone {
    position: absolute; left: 179px; top: 680px;
    font-family: "Roboto Condensed", sans-serif; font-weight: 700;
    font-size: 55px; line-height: 64px; color: var(--navy); letter-spacing: -0.5px;
    white-space: nowrap;
  }

  .firm-name {
    position: absolute; left: 597px; width: 220px; top: 172px; text-align: center;
    font-family: "Inter", sans-serif; font-weight: 500;
    font-size: 26px; color: var(--gold-deep); letter-spacing: 1px;
  }

  .code-box {
    position: absolute; left: 964px; top: 81px; width: 156px; height: 156px;
    border: 3px solid var(--navy);
  }
  .address-lines { position: absolute; left: 638px; top: 353px; width: 480px; list-style: none; }
  .address-lines li { height: 2px; background: var(--navy); margin-bottom: 70px; }

  .web-band {
    position: absolute; left: 597px; top: 700px; width: 603px; height: 44px;
    background: var(--navy);
    display: flex; align-items: center; justify-content: center;
  }
  .web-band span {
    font-family: "Inter", sans-serif; font-weight: 500; font-size: 25px;
    color: var(--white); letter-spacing: 13px; padding-left: 13px;
  }
</style>
</head>
<body>
<div class="postcard">
  <div class="frame"></div>
  <div class="photo" role="img" aria-label="Stock photo of an aggressive dog biting a person's hand"></div>

  <div class="info-panel"></div>

  <svg class="hours-icon" viewBox="0 0 94 94" aria-hidden="true">
    <path d="M78 22 A40 40 0 1 1 30 10" fill="none" stroke="var(--navy)" stroke-width="6"/>
    <path d="M24 2 L40 10 L26 20 Z" fill="var(--navy)"/>
    <circle cx="47" cy="50" r="32" fill="var(--navy)"/>
    <text x="47" y="59" text-anchor="middle" font-family="Roboto Condensed, sans-serif" font-weight="700" font-size="25" fill="var(--white)">24/7</text>
  </svg>
  <h2 class="headline">Available 24 hours a day<br>7 days per week.</h2>

  <p class="takeover">May also want to mention that we can take over your case from another lawyer if you are not satisfied with your current attorney</p>

  <svg class="contact-icon" viewBox="0 0 80 80" aria-hidden="true">
    <path d="M40 6 A32 32 0 1 0 62 62 L74 72 L68 54 A32 32 0 0 0 40 6 Z" fill="none" stroke="var(--navy)" stroke-width="7" stroke-linejoin="round"/>
    <text x="38" y="49" text-anchor="middle" font-family="Roboto Condensed, sans-serif" font-weight="700" font-size="28" fill="var(--navy)">or</text>
  </svg>
  <div class="phone">(555) 418-3062</div>

  <div class="firm-name">Walter Gimsby</div>

  <div class="code-box" aria-label="Reference code"></div>

  <ul class="address-lines">
    <li></li><li></li><li></li><li></li><li></li>
  </ul>

  <div class="web-band"><span>www.gimsbylaw.com</span></div>
</div>
</body>
</html>
```